Mental Health Therapy Website

I need a design for a mental health therapy website. It is a private practice. The business name is Fenwick Counseling, PLLC. My name is Martin Fenwick, LMHC, NCC, DCC. I would like some of the features/menus to be Home; Welcome/About Me, Rates and Services, Common Questions, and Contact.
If possible I would like a blog on the main page that I can update with articles I write. I would like the contact page to feature a map to my location (4318 Harbor Pine Ave. E, Lakewood, WA 98512).
I would like to place a small photo of me on the Welcome/About page.
I am new to this so if I am forgetting anything, please ask me!!
I will upload my logo so you can fit it and the color scheme into the design.
Thank you so very much!

```html
<!DOCTYPE html>
<html lang="en">
<head>
<meta charset="utf-8">
<title>Fenwick Counseling</title>
<link rel="stylesheet" href="https://fonts.googleapis.com/css2?family=Cinzel:wght@400;700&family=Open+Sans:wght@400;600&display=swap">
<style>
:root{
  --blue:#2b5c9c;
  --blue-dark:#24508a;
  --nav-top:#4279b8;
  --nav-bottom:#2a5893;
  --green:#5f9126;
  --green-nav:#7aab33;
  --text:#444;
  --muted:#666;
  --rule:#e2e2e2;
  --band:#f2f2f2;
  --footer:#2b2b2b;
}
*{box-sizing:border-box;margin:0;padding:0}
html,body{width:952px;height:1200px;overflow:hidden;background:#fff}
body{position:relative;font-family:"Open Sans",Arial,sans-serif;color:var(--text)}
.abs{position:absolute}
.heading{font-family:"Cinzel",Georgia,serif;color:var(--blue);font-size:20px;font-weight:400;letter-spacing:.3px}

/* header */
.brand{left:80px;top:22px;display:flex;align-items:center;gap:8px}
.brand-dot{width:40px;height:40px;border-radius:50%;background:var(--green)}
.brand-name{font-family:"Cinzel",Georgia,serif;font-size:24px;font-weight:700;color:var(--blue);line-height:1}
.call{right:79px;top:18px;font-size:15px;color:var(--green);font-weight:400}
.call b{color:var(--blue);font-weight:400}
.search{left:722px;top:48px;width:149px;height:25px;border:1px solid #ccc;font-size:10.5px;color:#999;padding:5px 8px}
.search svg{position:absolute;right:6px;top:5px}

/* nav */
.nav{left:0;top:91px;width:952px;height:41px;background:linear-gradient(var(--nav-top),var(--nav-bottom))}
.nav ul{list-style:none;position:absolute;left:80px;top:0;display:flex;height:41px}
.nav li{font-family:"Cinzel",Georgia,serif;font-weight:700;font-size:12.5px;color:#fff;height:41px;line-height:41px;text-align:center;border-right:1px solid rgba(0,0,0,.18)}
.nav li.active{background:var(--green-nav)}
.social{display:flex;gap:10px;position:absolute;left:782px;top:9px}
.social span{width:22px;height:22px;border-radius:50%;background:#fff;opacity:.85}

/* hero */
.hero{left:79px;top:141px;width:794px;height:304px;background:linear-gradient(90deg,#b9a48a 0%,#d8d1c6 45%,#e4e4ea 70%,#e8e8ee 100%)}
.hero-copy{right:119px;top:200px;text-align:right}
.hero-title{font-family:"Cinzel",Georgia,serif;font-size:19px;color:#333;letter-spacing:.4px}
.hero-text{margin-top:6px;font-size:11.5px;line-height:18.5px;color:#333}
.btn{display:inline-block;margin-top:12px;background:#fff;border:1px solid #ddd;color:var(--green);font-size:11px;padding:8px 15px;border-radius:2px}
.dots{left:783px;top:416px;display:flex;gap:9px}
.dots i{width:10px;height:10px;border-radius:50%;background:#aaa;box-shadow:inset 0 1px 2px rgba(0,0,0,.3)}
.dots i:first-child{background:#666}

/* welcome */
.welcome-title{left:80px;top:472px}
.welcome-text{left:82px;top:506px;width:618px;font-size:11.8px;line-height:20px;color:#555}
.portrait{left:714px;top:480px;width:158px;height:119px;border:1px solid #ddd;padding:4px;background:#fff}
.portrait div{width:100%;height:100%;background:linear-gradient(90deg,#eef1f5,#9aa1aa 45%,#eef1f5)}
.rule{left:80px;width:793px;height:1px;background:var(--rule)}

/* services */
.services-title{left:82px;top:646px}
.service{top:687px;width:180px;text-align:center}
.service .ph{height:110px}
.service p{margin-top:9px;color:var(--green);font-size:13.5px;font-weight:600}

/* articles */
.articles-title{left:81px;top:861px}
.next{left:859px;top:868px;width:13px;height:13px;border:1px solid #ddd;font-size:9px;color:var(--green);text-align:center;line-height:11px}
.article-img{left:80px;top:899px;width:181px;height:117px;background:linear-gradient(90deg,#3b4a55,#6f8a5a 70%,#8fae6c)}
.article{left:275px;top:899px;width:598px}
.article h3{font-size:12.5px;font-weight:400;color:var(--blue)}
.article p{margin-top:6px;font-size:10.6px;line-height:16.5px;color:#555}
.shares{display:flex;gap:9px;margin-top:9px;font-size:9px;align-items:center}
.pill{display:flex;align-items:center;gap:3px}
.pill b{font-weight:600;border:1px solid #bcc8d8;background:#eef2f7;color:#334;padding:1px 5px;border-radius:2px}
.pill span{border:1px solid #ccc;padding:1px 4px;color:#333;background:#fff}
.pill.share b{background:#e9563a;border-color:#e9563a;color:#fff}

/* contact band */
.band{left:0;top:1043px;width:952px;height:76px;background:var(--band)}
.info{top:1065px;display:flex;align-items:center;gap:10px;font-size:10.8px;color:#777;line-height:17px}

/* footer */
.footer{left:0;top:1119px;width:952px;height:81px;background:var(--footer)}
.foot-links{left:80px;top:1137px;font-size:10.5px;color:#ccc;word-spacing:2px}
.foot-links i{font-style:normal;margin:0 9px;color:#999}
.copy{left:80px;top:1166px;font-size:10.5px;color:#ccc}
.foot-social{left:770px;top:1148px;display:flex;gap:6px}
.foot-social span{width:21px;height:21px;border-radius:50%;background:#555}
</style>
</head>
<body>

<header>
  <div class="abs brand"><span class="brand-dot"></span><span class="brand-name">Fenwick<br>Counseling</span></div>
  <div class="abs call">Call us : <b>555 204 7381</b></div>
  <div class="abs search">Search
    <svg width="13" height="13" viewBox="0 0 13 13"><circle cx="5" cy="5" r="3.6" fill="none" stroke="#222" stroke-width="1.8"/><path d="M7.6 7.6l4 4" stroke="#222" stroke-width="2.2"/></svg>
  </div>
</header>

<nav class="abs nav">
  <ul>
    <li class="active" style="width:83px">Home</li>
    <li style="width:109px">About Me</li>
    <li style="width:180px">Rates and Services</li>
    <li style="width:189px">Common Questions</li>
    <li style="width:103px">Contact</li>
  </ul>
  <div class="social"><span></span><span></span><span></span></div>
</nav>

<section>
  <div class="abs hero" role="img" aria-label="Photo of a counselor comforting an elderly man holding a cane"></div>
  <div class="abs hero-copy">
    <div class="hero-title">Nunc Tristique Vulputate</div>
    <div class="hero-text">Donec pulvinar leo vel tortor lobortis adipiscing.<br>Quisque venenatis quam ut leo sollicitudin male-<br>suada. Nulla sed interdum mi, in egestas nisl.</div>
    <span class="btn">BOOK AN APPOINTMENT</span>
  </div>
  <div class="abs dots"><i></i><i></i><i></i><i></i></div>
</section>

<section>
  <h2 class="abs heading welcome-title">Welcome to Fenwick Counselling</h2>
  <p class="abs welcome-text">Mental health counseling/therapy for individuals (children, adolescents, adults), couples, and families.&nbsp; I am a trauma certified therapist that utilizes CBT+ to assist with trauma.&nbsp; My approach to therapy is psychodynamic that utilizes tools from CBT, Solutions-focused, Emotions-focused, and Psychoeducation therapies to assist clients managing depression, anxiety, truama, phobias, personality disorders, ADHD, self-injury,and communication issues.&nbsp; Sessions are typically 45 to 50 minutes in length.</p>
  <div class="abs portrait"><div role="img" aria-label="Portrait photo of the therapist in a suit"></div></div>
  <div class="abs rule" style="top:629px"></div>
</section>

<section>
  <h2 class="abs heading services-title">Our Services</h2>
  <div class="abs service" style="left:80px"><div class="ph" role="img" aria-label="Photo of a sad woman resting on a bench" style="background:linear-gradient(#8a8f94,#6b5a4e)"></div><p>DEPRESSION</p></div>
  <div class="abs service" style="left:284px"><div class="ph" role="img" aria-label="Photo of a woman holding her temple" style="background:linear-gradient(90deg,#bfe0f0,#f2e4dc)"></div><p>ANXIETY</p></div>
  <div class="abs service" style="left:488px"><div class="ph" role="img" aria-label="Photo of a worried young child" style="background:linear-gradient(90deg,#6d6570,#b8a48c)"></div><p>TRUAMA &amp; PHOBIAS</p></div>
  <div class="abs service" style="left:692px"><div class="ph" role="img" aria-label="Photo of a man holding photos of himself in different moods" style="background:linear-gradient(90deg,#7a6552,#3d4a66 55%,#a08060)"></div><p>PERSONALITY DISORDERS</p></div>
  <div class="abs rule" style="top:845px"></div>
</section>

<section>
  <h2 class="abs heading articles-title">Latest Articles</h2>
  <div class="abs next">›</div>
  <div class="abs article-img" role="img" aria-label="Photo of a pensive young man by a window"></div>
  <article class="abs article">
    <h3>Duis pulvinar eros, ac laoreet diam ullamcorper vulputate</h3>
    <p>Aliquam fringilla nunc id erat ornare, non cursus nibh tincidunt. Morbi vitae erat lectus. Maecenas et elit laoreet arcu scelerisque mollis ac a lorem. Vestibulum ante ipsum primis in faucibus orci luctus et ultrices posuere cubilia Curae; Morbi dignissim, massa ut commodo dapibus, lorem risus lobortis lorem, sed mattis velit erat et velit. Ut ac sem sed lectus suscipit pharetra eu eu nisl.</p>
    <div class="shares">
      <div class="pill"><b>Like</b><span>3k</span></div>
      <div class="pill"><b>Post</b><span>316</span></div>
      <div class="pill"><b>+1</b><span>81</span></div>
      <div class="pill share"><b>Share</b><span>4.6K</span></div>
    </div>
  </article>
</section>

<section class="abs band"></section>
<div class="abs info" style="left:89px">
  <svg width="19" height="24" viewBox="0 0 19 24"><rect x="1" y="2" width="17" height="21" fill="none" stroke="#999" stroke-width="1.6"/><path d="M6 2v9l3-2 3 2V2" fill="none" stroke="#999" stroke-width="1.4"/></svg>
  <span>55, Building name, streetname<br>City - Zip code</span></div>
<div class="abs info" style="left:311px;top:1072px">
  <svg width="24" height="24" viewBox="0 0 24 24"><path d="M4 3l5 1 1 5-3 2c2 4 4 6 8 8l2-3 5 1 1 5c-10 1-20-9-19-19z" fill="#999"/></svg>
  <span>Phone: 555 204 7390</span></div>
<div class="abs info" style="left:495px;top:1070px">
  <svg width="24" height="24" viewBox="0 0 24 24"><rect x="1" y="8" width="5" height="15" fill="#999"/><rect x="7" y="6" width="16" height="17" fill="none" stroke="#999" stroke-width="1.6"/><rect x="9" y="1" width="11" height="7" fill="none" stroke="#999" stroke-width="1.4"/><path d="M10 13h2M14 13h2M18 13h2M10 17h2M14 17h2M18 17h2" stroke="#999" stroke-width="2"/></svg>
  <span>Fax : 555 204 7395</span></div>
<div class="abs info" style="left:667px;top:1073px">
  <svg width="22" height="16" viewBox="0 0 22 16"><rect x="1" y="1" width="20" height="14" fill="#aaa"/><path d="M1 1l10 8 10-8" fill="none" stroke="#f2f2f2" stroke-width="1.4"/></svg>
  <span style="margin-left:6px">E-mail : hello@fenwickcounseling.example</span></div>

<footer>
  <div class="abs footer"></div>
  <div class="abs foot-links">Home<i>|</i>About Me<i>|</i>Rates and Services<i>|</i>Common Questions<i>|</i>Contact</div>
  <div class="abs copy">Copyright&nbsp; ©&nbsp; 2014&nbsp;&nbsp; Fenwick Counseling.&nbsp;&nbsp; All rights reserved.</div>
  <div class="abs foot-social"><span></span><span></span><span></span><span></span></div>
</footer>

</body>
</html>
```